creating a certificate for our flagship course

Hi,
We need a new certificate for our flagship course called Rising Tide. We have been running this course for 25 years this year and want to get something special that represents that. We need our logos incorporated and we love to have a compass or Koru incorporated in the certificate. We like something different from your standard certificate, but not too crazy.

The text should say something along the lines of:
This certificate is awarded to ....
For successfully completing and contributing to the three day Rising Tide programme.

signed:... date:...

to learn a bit more about this course and our company, please check our website. www.veldonmarstik.co.nz

Thank you!

attendees who completed our 3 day programme.

• Both our RT logo and our brand logo. a compass or a koru.
• a 25th year existence something on it.

```html
<!DOCTYPE html>
<html lang="en">
<head>
<meta charset="utf-8">
<title>Rising Tide Certificate</title>
<link href="https://fonts.googleapis.com/css2?family=Oswald:wght@700&family=Source+Sans+3:wght@400;600&display=swap" rel="stylesheet">
<style>
  :root {
    --page: #ffffff;
    --border: #8fe23c;
    --lime-light: #eefad0;
    --lime: #b4f23f;
    --lime-deep: #9fe82a;
    --panel-white: #fbfef2;
    --ink: #111111;
    --navy: #2c3152;
    --logo-square: #8fe23c;
    --brand-square: #8fe23c;
    --brand-text: #ffffff;
  }
  * { margin: 0; padding: 0; box-sizing: border-box; }
  html, body { width: 1200px; height: 927px; overflow: hidden; background: var(--page); }
  .certificate { position: relative; width: 1200px; height: 927px; font-family: "Source Sans 3", "Myriad Pro", sans-serif; color: var(--ink); }
  .backdrop { position: absolute; inset: 0; }
  .course-logo { position: absolute; left: 101px; top: 107px; display: flex; align-items: center; gap: 21px; }
  .course-logo__square { width: 104px; height: 94px; background: var(--logo-square); }
  .course-logo__name { font-size: 37px; font-weight: 400; color: var(--navy); letter-spacing: 0.2px; }
  .anniversary { position: absolute; left: 101px; top: 214px; font-size: 19px; font-weight: 600; color: var(--navy); letter-spacing: 2px; text-transform: uppercase; }
  .title { position: absolute; left: 549px; width: 509px; top: 136px; text-align: center; font-family: "Oswald", "Impact", sans-serif; font-weight: 700; font-size: 72px; letter-spacing: 6px; line-height: 1; }
  .award-line { position: absolute; left: 549px; width: 509px; top: 274px; text-align: center; font-size: 26px; }
  .recipient { position: absolute; left: 549px; width: 509px; top: 396px; border-top: 2px solid var(--ink); }
  .reason { position: absolute; left: 549px; width: 509px; top: 426px; text-align: center; font-size: 26px; line-height: 37px; }
  .field { position: absolute; left: 672px; width: 263px; text-align: center; font-size: 24px; border-top: 2px solid var(--ink); padding-top: 10px; line-height: 1; }
  .field--date { top: 621px; }
  .field--signature { top: 747px; }
  .brand-logo { position: absolute; left: 95px; top: 727px; display: flex; align-items: center; gap: 22px; }
  .brand-logo__square { width: 83px; height: 80px; background: var(--brand-square); }
  .brand-logo__name { font-size: 23px; font-weight: 600; color: var(--brand-text); line-height: 30px; letter-spacing: 1px; text-transform: uppercase; }
</style>
</head>
<body>
<main class="certificate">
  <svg class="backdrop" width="1200" height="927" viewBox="0 0 1200 927" aria-hidden="true">
    <defs>
      <linearGradient id="field-fill" x1="0" y1="0" x2="1" y2="1">
        <stop offset="0" stop-color="var(--lime-light)"/>
        <stop offset="0.5" stop-color="#d6f58a"/>
        <stop offset="1" stop-color="var(--lime-deep)"/>
      </linearGradient>
      <linearGradient id="panel-fill" x1="0" y1="0" x2="1" y2="0">
        <stop offset="0" stop-color="var(--panel-white)"/>
        <stop offset="0.35" stop-color="#e6fab0"/>
        <stop offset="1" stop-color="var(--lime)"/>
      </linearGradient>
      <linearGradient id="swoosh-fill" x1="0" y1="0" x2="1" y2="1">
        <stop offset="0" stop-color="#c9f06a"/>
        <stop offset="1" stop-color="#a6ea2e"/>
      </linearGradient>
      <radialGradient id="spiral-fill" cx="0.5" cy="0.5" r="0.5">
        <stop offset="0" stop-color="#d0f57a"/>
        <stop offset="1" stop-color="#b3ec45"/>
      </radialGradient>
    </defs>
    <rect x="32" y="32" width="1136" height="862" fill="url(#field-fill)"/>
    <path class="swoosh" d="M32 295 C230 320 420 420 540 575 L540 894 L32 894 Z" fill="url(#swoosh-fill)" opacity="0.85"/>
    <path class="swoosh swoosh--inner" d="M32 520 C220 470 420 520 540 600 L540 894 L32 894 Z" fill="#a8ea33" opacity="0.6"/>
    <ellipse class="spiral" cx="258" cy="660" rx="140" ry="108" fill="url(#spiral-fill)" role="img" aria-label="Large embossed koru spiral decoration"/>
    <path class="panel" d="M528 32 C555 250 505 520 518 700 C524 790 530 850 535 894 L1095 894 C1080 700 1105 450 1085 250 C1078 160 1070 80 1065 32 Z" fill="url(#panel-fill)"/>
    <path class="panel-edge" d="M1065 32 C1070 80 1078 160 1085 250 C1105 450 1080 700 1095 894 L1168 894 L1168 32 Z" fill="var(--lime-deep)"/>
    <rect class="border" x="32" y="32" width="1136" height="862" fill="none" stroke="var(--border)" stroke-width="20" role="img" aria-label="Ornamental scroll border"/>
  </svg>

  <div class="course-logo">
    <span class="course-logo__square"></span>
    <span class="course-logo__name">Rising Tide</span>
  </div>
  <p class="anniversary">Celebrating 25 Years</p>

  <h1 class="title">CERTIFICATE</h1>
  <p class="award-line">This certificate is awarded to</p>
  <div class="recipient"></div>
  <p class="reason">For successfully completing and<br>contributing to the three day<br>Rising Tide programme.</p>
  <div class="field field--date">DATE</div>
  <div class="field field--signature">SIGNATURE</div>

  <div class="brand-logo">
    <span class="brand-logo__square"></span>
    <span class="brand-logo__name">Veldon<br>Marstik &amp; Associates</span>
  </div>
</main>
</body>
</html>
```